Large corporation needs landing page for its employees with emotional and psychological problems

Vision:
Hello, we are a startup and would like to build a landing page and website in the mental health sector for a large corporation. In this site employees with emotional and psychological problems should quickly receive professional psychological support. This support takes the form of internal referrals from employees who are looking for help to qualified therapists, so that help can be provided quickly.
Furthermore, the employees get access to a tool where they can find out about topics in the mind health area and can also get help via webinars and podcasts. The employee should thus be able to take the hurdle to seek help and support in good time.
Therapists for whom the focus is on the urgency of providing quick help and support will work here in cooperation with the respective corporations.
Keywords:
• Help/Support
• overcome inhibitions
• Competent help
• Uncomplicated help
• Permanent access
• protected space
• Recognizing and naming emotional problems and actively tackling them
• get help
• mindfulness
• everyday helper
• Informative
• Anonymous
• compassion
• tolerance
• respect
• Appreciation
• empathy
• mindfulness
• protected space
• To be needed
• Like a lighthouse signal
What we need:
Landingpage
We need a landing page aimed at getting employees to contact psychological help. The call to action is to get in contact via a contact form.
Landing page content
There are several text modules:
• A heading/greeting
• A body of text at the beginning that explains the purpose of the page
• A bulleted text area describing the pain points and the solutions to them
Video:
The heart of the content will be a video explaining the need and inviting them to get in touch.
contact form:
It should be kept simple: first name, last name and email address
Legally required content:
General terms and conditions, data protection and imprint. These are only given as links in the footer.
In parallel, the Corporate Design should be adapted/extended:
Logo:
The font in the logo should be revised. The wings in the background remain.
Please adapt the logo for different uses:
• on a black background
• with transparent background
• favorite icon (browser)
• In square format for social media
Colors:
• develop a color chart based on the colors of the logo.
• please determine 2-3 main colors and the matching variations. I.e. transparent variations or light colors.
Typography:
Determine a decorative font and/or typography for headings and a text font. There should be no more than 3 fonts.
Industry/Entity Type
to recruit therapists as employees
Requirements
Should not have
- please not to playful design or typography - and max. 3 colors

```html
<!DOCTYPE html>
<html lang="en">
<head>
<meta charset="UTF-8">
<title>calm harbor – Support for Employees</title>
<link rel="stylesheet" href="https://fonts.googleapis.com/css2?family=Outfit:wght@300;400;500;600&display=swap">
<style>
:root{
  --teal:#0b4f5c;
  --teal-dark:#083f4a;
  --sky:#b4dbe6;
  --sky-soft:#d8edf3;
  --grey-bg:#f1f1f1;
  --ink:#1b1b1b;
  --text:#4a4a4a;
  --line:#d6d6d6;
  --red:#d9232a;
  --green:#4caf2f;
  --white:#ffffff;
}
*{box-sizing:border-box;margin:0;padding:0}
html,body{width:1200px;height:3421px;overflow:hidden}
body{position:relative;font-family:"Outfit",sans-serif;color:var(--text);background:var(--white)}
.abs{position:absolute}

/* header */
.site-header{position:absolute;left:0;top:0;width:1200px;height:104px;background:var(--white)}
.brand{position:absolute;left:141px;top:30px;font-size:40px;font-weight:500;color:var(--teal);letter-spacing:-0.5px;line-height:1}
.head-contact{position:absolute;top:36px;display:flex;align-items:center;gap:10px}
.head-contact .icon{width:34px;height:34px;border-radius:50%;background:var(--teal);display:flex;align-items:center;justify-content:center}
.head-contact .label{font-size:12px;font-weight:600;color:var(--ink);letter-spacing:.3px}
.head-contact .value{font-size:14px;color:var(--text)}

/* hero */
.hero{position:absolute;left:0;top:104px;width:1200px;height:626px;overflow:hidden}
.hero-photo{position:absolute;inset:0;background:linear-gradient(90deg,#f3f6f8 0%,#e7eef2 40%,#c9d6dd 62%,#dfe8ed 78%,#aebcc4 100%)}
.hero-person{position:absolute;left:660px;top:50px;width:360px;height:560px;border-radius:180px 180px 0 0;background:linear-gradient(180deg,#c9a27a 0%,#b88b63 30%,#2a2d33 55%,#1c1f24 100%);opacity:.85}
.hero-copy{position:absolute;left:143px;top:100px;width:520px}
.hero-copy h1{font-size:27px;line-height:38px;font-weight:600;color:var(--ink)}
.hero-copy p{margin-top:12px;font-size:16px;line-height:23px;color:var(--ink)}
.btn{display:inline-block;background:var(--teal);color:var(--white);font-size:12px;font-weight:600;text-transform:uppercase;letter-spacing:.3px;border-radius:3px;text-align:center}
.hero-copy .btn{margin-top:18px;width:123px;height:38px;line-height:38px}
.hero-wave{position:absolute;left:0;top:104px;width:1200px;height:626px;pointer-events:none}

/* intro */
.media{position:absolute;border-radius:6px}
.intro-art{left:141px;top:716px;width:434px;height:320px;background:radial-gradient(circle at 55% 40%,#c9ecd6 0%,#8fc3ab 22%,#2c4a4f 45%,#1a2a30 75%,#142026 100%)}
.copy-block{position:absolute;width:428px}
.copy-block h2{font-size:27px;line-height:37px;font-weight:500;color:var(--teal)}
.copy-block p{margin-top:14px;font-size:12.5px;line-height:21.5px;color:var(--text)}
.copy-block p+p{margin-top:9px}

/* cards */
.card{position:absolute;top:1128px;width:297px;height:312px;border:1px solid #dfe9ec;border-radius:5px;background:var(--white);overflow:hidden}
.card-head{height:90px;background:var(--sky);display:flex;align-items:center;justify-content:center;font-size:25px;font-weight:500;color:var(--teal)}
.card ul{list-style:none;padding:26px 0 0 20px}
.card li{display:flex;align-items:center;gap:9px;height:34px;font-size:11.5px;color:var(--text)}

/* video */
.video-band{position:absolute;left:0;top:1528px;width:1200px;height:662px;background:var(--grey-bg)}
.section-title{position:absolute;left:0;width:1200px;text-align:center;font-size:35px;font-weight:500;color:var(--teal);letter-spacing:.3px}
.video{position:absolute;left:191px;top:1688px;width:812px;height:406px;border-radius:8px;overflow:hidden}
.video-still{position:absolute;inset:0;background:linear-gradient(100deg,#6f7a80 0%,#c9ccc8 30%,#e6e3dc 50%,#b8bfc2 70%,#7d878c 100%)}
.video-play{position:absolute;left:374px;top:180px;width:62px;height:44px;border:3px solid var(--white);border-radius:10px;display:flex;align-items:center;justify-content:center}
.video-bar{position:absolute;left:6px;right:6px;bottom:8px;height:24px;display:flex;align-items:center;gap:8px}
.video-bar .play{width:44px;height:24px;background:rgba(0,0,0,.75);border-radius:3px;display:flex;align-items:center;justify-content:center}
.video-bar .track{flex:1;height:24px;background:rgba(0,0,0,.55);border-radius:3px;position:relative}
.video-bar .track::before{content:"";position:absolute;left:6px;right:80px;top:11px;height:3px;background:rgba(255,255,255,.35)}
.video-bar .time{position:absolute;left:4px;top:-8px;font-size:9px;color:var(--white);background:#222;padding:0 3px}
.video-bar .hd{position:absolute;right:40px;top:5px;font-size:11px;font-weight:600;color:var(--white)}

.session-art{left:624px;top:2282px;width:434px;height:320px;background:linear-gradient(135deg,#2c4a55 0%,#3d5c66 40%,#4f8c90 65%,#c8a35a 80%,#2d5060 100%)}

/* form */
.field{position:absolute;height:42px;border:1px solid var(--line);border-radius:3px;background:var(--white);display:flex;align-items:center}
.field .ico{width:36px;height:100%;border-right:1px solid var(--line);display:flex;align-items:center;justify-content:center}
.field span{padding-left:18px;font-size:12px;color:#555}
.field.message{align-items:flex-start;height:85px}
.field.message .ico{height:42px;border-right:none}
.field.message span{padding-top:14px;padding-left:18px}
.submit{position:absolute;left:538px;top:2970px;width:124px;height:38px;line-height:38px}

/* footer */
.footer-wave{position:absolute;left:0;top:3030px;width:1200px;height:391px}
.footer-brand{position:absolute;left:0;top:3172px;width:1200px;text-align:center;font-size:40px;font-weight:500;color:var(--white);letter-spacing:-0.5px}
.foot-contact{position:absolute;top:3264px;display:flex;align-items:center;gap:14px;color:var(--white)}
.foot-contact .icon{width:44px;height:44px;border:1.5px solid var(--white);border-radius:50%;display:flex;align-items:center;justify-content:center}
.foot-contact .label{font-size:14px;font-weight:600}
.foot-contact .value{font-size:13px;line-height:19px}
.footer-rule{position:absolute;left:143px;top:3363px;width:915px;height:1px;background:rgba(255,255,255,.18)}
.copyright{position:absolute;left:143px;top:3383px;font-size:12.5px;color:var(--white)}
.legal{position:absolute;right:142px;top:3383px;font-size:12.5px;color:var(--white);display:flex;gap:18px}
</style>
</head>
<body>

<header class="site-header">
  <div class="brand">calm harbor</div>
  <div class="head-contact" style="left:682px">
    <div class="icon"><svg width="16" height="16" viewBox="0 0 24 24"><path fill="#fff" d="M6.6 10.8a15.1 15.1 0 0 0 6.6 6.6l2.2-2.2a1 1 0 0 1 1-.25 11.4 11.4 0 0 0 3.6.57 1 1 0 0 1 1 1V20a1 1 0 0 1-1 1A17 17 0 0 1 3 4a1 1 0 0 1 1-1h3.5a1 1 0 0 1 1 1c0 1.25.2 2.45.57 3.57a1 1 0 0 1-.25 1z"/></svg></div>
    <div><div class="label">PHONE</div><div class="value">123-456-7890</div></div>
  </div>
  <div class="head-contact" style="left:860px">
    <div class="icon"><svg width="16" height="16" viewBox="0 0 24 24"><path fill="#fff" d="M3 5h18v14H3z"/><path fill="none" stroke="#0b4f5c" stroke-width="1.8" d="M3 6l9 7 9-7"/></svg></div>
    <div><div class="label">EMAIL</div><div class="value">info@calmharbor.com</div></div>
  </div>
</header>

<section class="hero">
  <div class="hero-photo" role="img" aria-label="Bright modern office with a smiling professional woman in a dark blazer, arms crossed"></div>
  <div class="hero-person" aria-hidden="true"></div>
  <div class="hero-copy">
    <h1>We Help Employees With Emotional &amp; Psychological Problems To Quickly Receive Professional Psychological Support</h1>
    <p>The employees get access to a tool where they can find out about topics in the mind health area and can also get help via webinars and podcasts.</p>
    <a class="btn">Contact Us</a>
  </div>
</section>
<svg class="hero-wave" viewBox="0 0 1200 626" aria-hidden="true">
  <path fill="#b4dbe6" d="M0 368 C250 456 500 481 760 496 C950 511 1100 566 1200 616 L1200 626 L0 626 Z"/>
  <path fill="#ffffff" d="M0 564 C120 486 330 471 620 481 C900 491 1080 546 1200 618 L1200 626 L0 626 Z"/>
  <path fill="none" stroke="#ffffff" stroke-width="4" d="M0 368 C250 456 500 481 760 496 C950 511 1100 566 1200 616"/>
</svg>

<div class="media intro-art" role="img" aria-label="Illustration of a head silhouette opening onto a glowing tree over misty green hills inside a dark cave"></div>
<div class="copy-block" style="left:634px;top:740px">
  <h2>Ut Wisi Enim Ad Min Veniam Quis Nostrud Exerci.</h2>
  <p>Lorem ipsum dolor sit amet, consectetuer adipiscing elit sed nonuy nibh euismod tincidunt ut laoreet do magna.</p>
  <p>Ut wisi enim ad minim veniam, quis nostrud exerci tati ullamcorper suscipit lobortis nisl ut aliquip ex ea commodo conquat. Duis autem vel eum iriure dolor in hendrerit in vulputate velitsse tie consequat, vel illum dolore eu feugiat nulla facilisis at vero eros et accumsan et iusto odio dignissim qui blandit praesent luptatum zzril delnit augue duis dolore te feugait nulla facilisi.</p>
</div>

<div class="card" style="left:280px">
  <div class="card-head">Pain Points</div>
  <ul>
    <li><svg width="10" height="10" viewBox="0 0 10 10"><path stroke="#d9232a" stroke-width="2.2" d="M2 2l6 6M8 2l-6 6"/></svg>Consectetuer Adipiscing Elit</li>
    <li><svg width="10" height="10" viewBox="0 0 10 10"><path stroke="#d9232a" stroke-width="2.2" d="M2 2l6 6M8 2l-6 6"/></svg>Laoreet Dolore Magna Aliquam</li>
    <li><svg width="10" height="10" viewBox="0 0 10 10"><path stroke="#d9232a" stroke-width="2.2" d="M2 2l6 6M8 2l-6 6"/></svg>Quis Nostrud Exerci Ton Ullamcorper</li>
    <li><svg width="10" height="10" viewBox="0 0 10 10"><path stroke="#d9232a" stroke-width="2.2" d="M2 2l6 6M8 2l-6 6"/></svg>Duis Autem Vel Eum Iriure Do Hendrerit</li>
    <li><svg width="10" height="10" viewBox="0 0 10 10"><path stroke="#d9232a" stroke-width="2.2" d="M2 2l6 6M8 2l-6 6"/></svg>Ut Laoreet Dolore Magna Aliquam Erat</li>
  </ul>
</div>
<div class="card" style="left:623px">
  <div class="card-head">Our Solutions</div>
  <ul>
    <li><svg width="11" height="10" viewBox="0 0 11 10"><path fill="none" stroke="#4caf2f" stroke-width="2.2" d="M1.5 5l3 3 5-6"/></svg>Consectetuer Adipiscing Elit</li>
    <li><svg width="11" height="10" viewBox="0 0 11 10"><path fill="none" stroke="#4caf2f" stroke-width="2.2" d="M1.5 5l3 3 5-6"/></svg>Laoreet Dolore Magna Aliquam</li>
    <li><svg width="11" height="10" viewBox="0 0 11 10"><path fill="none" stroke="#4caf2f" stroke-width="2.2" d="M1.5 5l3 3 5-6"/></svg>Quis Nostrud Exerci Ton Ullamcorper</li>
    <li><svg width="11" height="10" viewBox="0 0 11 10"><path fill="none" stroke="#4caf2f" stroke-width="2.2" d="M1.5 5l3 3 5-6"/></svg>Duis Autem Vel Eum Iriure Do Hendrerit</li>
    <li><svg width="11" height="10" viewBox="0 0 11 10"><path fill="none" stroke="#4caf2f" stroke-width="2.2" d="M1.5 5l3 3 5-6"/></svg>Ut Laoreet Dolore Magna Aliquam Erat</li>
  </ul>
</div>

<section class="video-band"></section>
<h2 class="section-title" style="top:1606px">WATCH VIDEO</h2>
<div class="video">
  <div class="video-still" role="img" aria-label="Video still of a group of young colleagues sitting together and talking cheerfully"></div>
  <div class="video-play"><svg width="22" height="24" viewBox="0 0 22 24"><path fill="none" stroke="#fff" stroke-width="3" stroke-linejoin="round" d="M4 3l15 9-15 9z"/></svg></div>
  <div class="video-bar">
    <div class="play"><svg width="10" height="12" viewBox="0 0 10 12"><path fill="#fff" d="M0 0l10 6-10 6z"/></svg></div>
    <div class="track"><span class="time">1:32</span><span class="hd">HD</span></div>
  </div>
</div>

<div class="copy-block" style="left:143px;top:2305px">
  <h2>Ut Wisi Enim Ad Min Veniam Quis Nostrud Exerci.</h2>
  <p>Lorem ipsum dolor sit amet, consectetuer adipiscing elit sed nonuy nibh euismod tincidunt ut laoreet do magna.</p>
  <p>Ut wisi enim ad minim veniam, quis nostrud exerci tati ullamcorper suscipit lobortis nisl ut aliquip ex ea commodo conquat. Duis autem vel eum iriure dolor in hendrerit in vulputate velitsse tie consequat, vel illum dolore eu feugiat nulla facilisis at vero eros et accumsan et iusto odio dignissim qui blandit praesent luptatum zzril delnit augue duis dolore te feugait nulla facilisi.</p>
</div>
<div class="media session-art" role="img" aria-label="Woman on a sofa in a cosy living room holding a tablet during an online therapy session"></div>

<h2 class="section-title" style="top:2684px">CONTACT US</h2>
<form>
  <div class="field" style="left:303px;top:2751px;width:289px">
    <div class="ico"><svg width="12" height="12" viewBox="0 0 12 12"><circle cx="6" cy="3.2" r="2.8" fill="#0b4f5c"/><path fill="#0b4f5c" d="M0.5 12c0-3.3 2.5-5 5.5-5s5.5 1.7 5.5 5z"/></svg></div><span>First Name*</span></div>
  <div class="field" style="left:607px;top:2751px;width:290px">
    <div class="ico"><svg width="12" height="12" viewBox="0 0 12 12"><circle cx="6" cy="3.2" r="2.8" fill="#0b4f5c"/><path fill="#0b4f5c" d="M0.5 12c0-3.3 2.5-5 5.5-5s5.5 1.7 5.5 5z"/></svg></div><span>Last Name*</span></div>
  <div class="field" style="left:303px;top:2806px;width:289px">
    <div class="ico"><svg width="12" height="12" viewBox="0 0 24 24"><path fill="#0b4f5c" d="M6.6 10.8a15.1 15.1 0 0 0 6.6 6.6l2.2-2.2a1 1 0 0 1 1-.25 11.4 11.4 0 0 0 3.6.57 1 1 0 0 1 1 1V20a1 1 0 0 1-1 1A17 17 0 0 1 3 4a1 1 0 0 1 1-1h3.5a1 1 0 0 1 1 1c0 1.25.2 2.45.57 3.57a1 1 0 0 1-.25 1z"/></svg></div><span>Your Phone*</span></div>
  <div class="field" style="left:607px;top:2806px;width:290px">
    <div class="ico"><svg width="13" height="10" viewBox="0 0 13 10"><rect width="13" height="10" rx="1" fill="#0b4f5c"/><path fill="none" stroke="#fff" stroke-width="1.2" d="M0.5 1l6 4.5 6-4.5"/></svg></div><span>Your Email*</span></div>
  <div class="field message" style="left:303px;top:2861px;width:594px">
    <div class="ico"><svg width="14" height="12" viewBox="0 0 14 12"><ellipse cx="5.5" cy="4.5" rx="5.2" ry="4" fill="#0b4f5c"/><ellipse cx="9.5" cy="7.5" rx="4.2" ry="3.3" fill="#0b4f5c"/></svg></div><span>Your Message</span></div>
  <a class="btn submit">Submit Now</a>
</form>

<footer>
  <svg class="footer-wave" viewBox="0 0 1200 391" aria-hidden="true">
    <path fill="#0b4f5c" d="M0 135 C250 70 520 95 760 80 C960 68 1100 40 1200 6 L1200 391 L0 391 Z"/>
  </svg>
  <div class="footer-brand">calm harbor</div>
  <div class="foot-contact" style="left:257px">
    <div class="icon"><svg width="18" height="18" viewBox="0 0 24 24"><path fill="#fff" d="M6.6 10.8a15.1 15.1 0 0 0 6.6 6.6l2.2-2.2a1 1 0 0 1 1-.25 11.4 11.4 0 0 0 3.6.57 1 1 0 0 1 1 1V20a1 1 0 0 1-1 1A17 17 0 0 1 3 4a1 1 0 0 1 1-1h3.5a1 1 0 0 1 1 1c0 1.25.2 2.45.57 3.57a1 1 0 0 1-.25 1z"/></svg></div>
    <div><div class="label">PHONE</div><div class="value">123-456-7890</div></div>
  </div>
  <div class="foot-contact" style="left:488px;top:3256px">
    <div class="icon"><svg width="16" height="20" viewBox="0 0 16 20"><path fill="none" stroke="#fff" stroke-width="1.8" d="M8 19s-6.5-7-6.5-11a6.5 6.5 0 0 1 13 0c0 4-6.5 11-6.5 11z"/><circle cx="8" cy="8" r="2.3" fill="#fff"/></svg></div>
    <div><div class="label">ADDRESS</div><div class="value">123 Lorem Ipsum Dolor Sit<br>Consectetuer Adipiscing.</div></div>
  </div>
  <div class="foot-contact" style="left:798px">
    <div class="icon"><svg width="18" height="14" viewBox="0 0 18 14"><rect x="1" y="1" width="16" height="12" fill="none" stroke="#fff" stroke-width="1.6"/><path fill="none" stroke="#fff" stroke-width="1.6" d="M1 1.5l8 6 8-6M1 13l6-5M17 13l-6-5"/></svg></div>
    <div><div class="label">EMAIL</div><div class="value">info@calmharbor.com</div></div>
  </div>
  <div class="footer-rule"></div>
  <div class="copyright">© 2023 calm harbor. All Rights Reserved.</div>
  <div class="legal"><span>Terms And Conditions</span><span>I</span><span>Data Protection</span><span>I</span><span>Imprint</span></div>
</footer>

</body>
</html>
```